Surviving Domestic Violence Flyer

I need a flyer that "POPS" to attract participants for my research project. I have added the important information on my draft flyer.

```html
<!DOCTYPE html>
<html lang="en">
<head>
<meta charset="utf-8">
<title>Request for Study Participants</title>
<link rel="stylesheet" href="https://fonts.googleapis.com/css2?family=Oswald:wght@600&family=Roboto+Condensed:wght@700&family=Arimo:wght@400;700&display=swap">
<style>
  :root {
    --page: #ffffff;
    --ink: #050505;
    --ink-soft: #1c1c1c;
    --teal: #1ab0b0;
    --white: #ffffff;
    --grey-text: #d6d6d6;
    --rule: #8a8a8a;
  }
  * { box-sizing: border-box; margin: 0; padding: 0; }
  html, body { width: 1200px; height: 900px; overflow: hidden; background: var(--page); }
  .flyer {
    position: absolute; left: 265px; top: 18px; width: 643px; height: 833px;
    background: radial-gradient(ellipse at 55% 35%, var(--ink-soft) 0%, var(--ink) 75%);
    font-family: "Arimo", Arial, sans-serif; color: var(--white); overflow: hidden;
  }
  .title {
    position: absolute; left: 50%; top: 16px;
    transform: translateX(-50%) scaleX(0.74); transform-origin: center top;
    white-space: nowrap;
    font-family: "Oswald", "Impact", sans-serif; font-weight: 600; font-size: 60px;
    line-height: 1; color: var(--teal); letter-spacing: 0;
  }
  .subtitle {
    position: absolute; left: 0; width: 100%; top: 81px; text-align: center;
    white-space: nowrap;
    font-family: "Roboto Condensed", Arial, sans-serif; font-weight: 700; font-size: 15.5px;
    letter-spacing: 0.6px; text-transform: uppercase;
  }
  .questions { position: absolute; left: 98px; top: 134px; list-style: none; font-size: 17.3px; line-height: 20px; }
  .questions li { margin-bottom: 12px; white-space: nowrap; }
  .questions li:nth-child(odd) { color: var(--teal); }
  .questions li:nth-child(even) { color: var(--white); }
  .eligibility {
    position: absolute; left: 35px; top: 335px; width: 590px;
    font-size: 12.5px; line-height: 15.5px; color: var(--grey-text);
  }
  .photo {
    position: absolute; left: 0; top: 372px; width: 300px; height: 318px;
    background: radial-gradient(ellipse at 30% 45%, #7a7a7a 0%, #3c3c3c 45%, rgba(5,5,5,0) 80%);
  }
  .contact { position: absolute; left: 314px; top: 411px; width: 320px; }
  .contact-lead { font-size: 19px; line-height: 24px; white-space: nowrap; }
  .contact-phone { font-size: 25px; line-height: 30px; width: 282px; text-align: center; }
  .small { font-size: 11.5px; line-height: 14px; }
  .teal { color: var(--teal); }
  .compensation { margin-top: 30px; }
  .investigator { margin-top: 28px; }
  .tabs {
    position: absolute; left: 0; top: 691px; width: 100%; height: 142px;
    border-top: 1px solid var(--rule); display: flex; background: var(--ink);
  }
  .tab {
    flex: 1; border-right: 1px dashed var(--rule);
    display: flex; justify-content: center; align-items: flex-end; padding: 6px 0 10px;
  }
  .tab:last-child { border-right: none; }
  .tab-text {
    writing-mode: vertical-rl; transform: rotate(180deg);
    display: flex; flex-direction: column; gap: 1px; text-align: left; white-space: nowrap;
  }
  .tab-label { font-size: 10px; font-weight: 700; }
  .tab-phone { font-size: 14.5px; font-weight: 700; }
</style>
</head>
<body>
<main class="flyer">
  <h1 class="title">Request for Study Participants</h1>
  <p class="subtitle">Efficiency of resources available to suvivors of intimate partner abuse</p>

  <ul class="questions">
    <li>Are you eighteen years of age or older?</li>
    <li>Have you been a victim of domestic violence?</li>
    <li>Have you sought assistance with abuse in last 12 months?</li>
    <li>Are you still in contact with person who abused you?</li>
    <li>Are you willing and open to discussing your expirience with<br>abuse and your attempts to access services or resources?</li>
  </ul>

  <p class="eligibility">If you answered yes to all of these questions, you may be eligible to participate in a study to better understand the resources needed and services expected for survivors of domestic violence.</p>

  <div class="photo" role="img" aria-label="Black and white photo of a distressed woman holding her hand to her head"></div>

  <section class="contact">
    <p class="contact-lead">Please contact Dana Whitfield at</p>
    <p class="contact-phone">1(555)214-0386</p>
    <p class="small">via e-mail <span class="teal">survivorvoicesstudy@example.com</span><br>for additional information.</p>
    <p class="small compensation">Participants will be comensated for their time.</p>
    <p class="small investigator">
      <span class="teal">Principal Investigator:</span><br>
      Dana Whitfield<br>
      Institutional Affiliation: Lakeshore State University,<br>
      Dept. of Criminology, Law and Justice<br>
      <span class="teal">Contact Address:</span><br>
      Post Office Box 100200, Chicago, IL, 60601
    </p>
  </section>

  <div class="tabs">
    <div class="tab"><div class="tab-text"><span class="tab-label">Survivor Resources Study</span><span class="tab-phone">1(555)214-0386</span></div></div>
    <div class="tab"><div class="tab-text"><span class="tab-label">Survivor Resources Study</span><span class="tab-phone">1(555)214-0386</span></div></div>
    <div class="tab"><div class="tab-text"><span class="tab-label">Survivor Resources Study</span><span class="tab-phone">1(555)214-0386</span></div></div>
    <div class="tab"><div class="tab-text"><span class="tab-label">Survivor Resources Study</span><span class="tab-phone">1(555)214-0386</span></div></div>
    <div class="tab"><div class="tab-text"><span class="tab-label">Survivor Resources Study</span><span class="tab-phone">1(555)214-0386</span></div></div>
    <div class="tab"><div class="tab-text"><span class="tab-label">Survivor Resources Study</span><span class="tab-phone">1(555)214-0386</span></div></div>
    <div class="tab"><div class="tab-text"><span class="tab-label">Survivor Resources Study</span><span class="tab-phone">1(555)214-0386</span></div></div>
    <div class="tab"><div class="tab-text"><span class="tab-label">Survivor Resources Study</span><span class="tab-phone">1(555)214-0386</span></div></div>
    <div class="tab"><div class="tab-text"><span class="tab-label">Survivor Resources Study</span><span class="tab-phone">1(555)214-0386</span></div></div>
    <div class="tab"><div class="tab-text"><span class="tab-label">Survivor Resources Study</span><span class="tab-phone">1(555)214-0386</span></div></div>
    <div class="tab"><div class="tab-text"><span class="tab-label">Survivor Resources Study</span><span class="tab-phone">1(555)214-0386</span></div></div>
    <div class="tab"><div class="tab-text"><span class="tab-label">Survivor Resources Study</span><span class="tab-phone">1(555)214-0386</span></div></div>
    <div class="tab"><div class="tab-text"><span class="tab-label">Survivor Resources Study</span><span class="tab-phone">1(555)214-0386</span></div></div>
  </div>
</main>
</body>
</html>
```